Outdoor sign for Brindle Auto Restoration

I need a horizontal 4'x 8' outdoor roadside sign for my classic auto restoration business. I have uploaded colors and our logo. Needs the Brindle name, a prominent Classic AUTO RESTORATION, phone number and website. We rebuild and restore vintage cars, trucks and 4x4s. I'd like something clean but possibly retro. Classic Auto Restoration is more important than the Brindle name. It needs to be visible and readable from the street. NO CLIP ART

Target Market(s)

Customers who need their vintage care restored or upgraded. Men and women ages 25-75

Industry/Entity Type

Automotive

Colors
FFC000
F8CF3A
FAE287
FDF2CF
FEFAEE

Requirements
Must have
• Legible. Bright. Readable as a backlit 4' x 8' large horizontal sign (roughly 120cm X 240cm)
Nice to have
• Use of the Brindle logo/type, Complete or Classic before prominent AUTO RESTORATION
Should not have
• Clip art of old cars or icons. And we don't want the Brindle Logo from the website because it wont be legible from the road. I have included the Illustrator file for Brindle text in the uploads

```html
<!DOCTYPE html>
<html lang="en">
<head>
<meta charset="utf-8">
<title>Brindle Auto Restoration – Roadside Sign</title>
<link href="https://fonts.googleapis.com/css2?family=Anton&family=Lobster&family=Roboto+Condensed:wght@600;800&display=swap" rel="stylesheet">
<style>
  :root {
    --page: #ffffff;
    --sign-black: #000000;
    --amber: #f5b002;
    --amber-soft: #f8c02a;
    --white: #ffffff;
  }
  html, body {
    margin: 0;
    padding: 0;
    width: 1200px;
    height: 600px;
    overflow: hidden;
    background: var(--page);
  }
  .sign {
    display: block;
    width: 1200px;
    height: 600px;
  }
  .sign-panel { fill: var(--sign-black); }
  .feature-area { fill: url(#feature-fill); }
  .tagline-script {
    font-family: "Lobster", cursive;
    font-size: 50px;
    fill: var(--white);
  }
  .headline {
    font-family: "Anton", "Impact", sans-serif;
    font-size: 158px;
    letter-spacing: 1px;
  }
  .headline-shadow { fill: var(--sign-black); }
  .headline-face { fill: var(--white); }
  .contact {
    font-family: "Roboto Condensed", "Arial Narrow", sans-serif;
    font-weight: 600;
    font-size: 33px;
    fill: var(--white);
  }
  .contact-dot { fill: var(--amber); }
  .brand-name {
    font-family: "Roboto Condensed", "Arial Narrow", sans-serif;
    font-weight: 800;
    font-size: 56px;
    letter-spacing: 1px;
    fill: var(--amber);
  }
</style>
</head>
<body>
<svg class="sign" viewBox="0 0 1200 600" xmlns="http://www.w3.org/2000/svg" aria-label="Brindle Classic Auto Restoration roadside sign">
  <defs>
    <linearGradient id="feature-fill" x1="0" y1="0" x2="0" y2="1">
      <stop offset="0" stop-color="var(--amber-soft)"/>
      <stop offset="1" stop-color="var(--amber)"/>
    </linearGradient>
  </defs>

  <rect class="sign-panel" x="120" y="60" width="968" height="484"/>

  <rect class="feature-area" x="176" y="135" width="857" height="276" role="img" aria-label="Retro amber graphic panel with converging road stripes behind the headline"/>

  <text class="tagline-script" x="604" y="177" text-anchor="middle">Classic</text>

  <text class="headline headline-shadow" x="222" y="350" textLength="762" lengthAdjust="spacingAndGlyphs">AUTO RESTORATION</text>
  <text class="headline headline-face" x="229" y="343" textLength="762" lengthAdjust="spacingAndGlyphs">AUTO RESTORATION</text>

  <text class="contact" x="209" y="502" textLength="167" lengthAdjust="spacingAndGlyphs">501-555-0147</text>
  <circle class="contact-dot" cx="398" cy="490" r="4.5"/>
  <text class="contact" x="414" y="502" textLength="290" lengthAdjust="spacingAndGlyphs">brindleautoworks.com</text>

  <text class="brand-name" x="736" y="502" textLength="266" lengthAdjust="spacingAndGlyphs">BRINDLE</text>
</svg>
</body>
</html>
```